Dockhavenly is a new company, currently under development opening in June. We store & repair shi

This is our first draft of what we want to present & it is very basic.
Our clients are shipping lines and we would like something with a bit of flair. We had the logo designed so those colours of yellow & grey are non negotiable. We are looking for background colours, heading designs etc to blend in whilst incorporating an image of sustainability, moving forward into the future and offering professional service.

Industry/Entity Type

Shipping

```html
<!DOCTYPE html>
<html lang="en">
<head>
<meta charset="utf-8">
<title>Dockhavenly – Opening in Melbourne</title>
<link rel="stylesheet" href="https://fonts.googleapis.com/css2?family=Arimo:ital,wght@0,400;1,400&family=Lato:ital,wght@0,700;1,400&display=swap">
<style>
  :root {
    --slate-dark: #2e2e2e;
    --slate-mid: #5a5a5a;
    --headline: #f4f4f4;
    --tagline: #bdbdbd;
    --rule-white: #ffffff;
    --leaf-green: #8fd63a;
    --leaf-green-light: #b6e86a;
    --sun-yellow: #f6c21a;
    --sun-yellow-light: #fbd94a;
    --footer-ink: #1c1c1c;
  }
  html, body {
    margin: 0;
    padding: 0;
    overflow: hidden;
    background: #ffffff;
  }
  .announcement {
    position: relative;
    width: 1200px;
    height: 903px;
    overflow: hidden;
    background: radial-gradient(ellipse 70% 65% at 50% 58%, var(--slate-mid), var(--slate-dark));
  }
  .base-bands {
    position: absolute;
    left: 0;
    top: 0;
    width: 1200px;
    height: 903px;
  }
  .headline {
    position: absolute;
    left: 115px;
    margin: 0;
    font-family: "Arimo", Arial, sans-serif;
    font-weight: 400;
    font-size: 69px;
    line-height: 1;
    color: var(--headline);
    letter-spacing: 0.5px;
    white-space: nowrap;
  }
  .headline--italic { font-style: italic; }
  .headline--new { top: 104px; }
  .headline--exciting { top: 196px; }
  .headline--and { top: 388px; }
  .headline--opening { top: 486px; }
  .tagline {
    position: absolute;
    right: 95px;
    top: 589px;
    margin: 0;
    font-family: "Lato", "Gill Sans", sans-serif;
    font-style: italic;
    font-size: 23px;
    color: var(--tagline);
    white-space: nowrap;
  }
  .footer-detail {
    position: absolute;
    top: 862px;
    margin: 0;
    font-family: "Lato", "Gill Sans", sans-serif;
    font-weight: 700;
    font-size: 17px;
    color: var(--footer-ink);
    white-space: nowrap;
  }
  .footer-detail--address { left: 30px; }
  .footer-detail--web { right: 25px; }
</style>
</head>
<body>
<main class="announcement">
  <svg class="base-bands" viewBox="0 0 1200 903" aria-hidden="true">
    <defs>
      <linearGradient id="yellowBand" x1="0" y1="0" x2="0" y2="1">
        <stop offset="0" stop-color="var(--sun-yellow-light)"/>
        <stop offset="1" stop-color="var(--sun-yellow)"/>
      </linearGradient>
      <linearGradient id="greenBand" x1="0" y1="0" x2="0" y2="1">
        <stop offset="0" stop-color="var(--leaf-green-light)"/>
        <stop offset="1" stop-color="var(--leaf-green)"/>
      </linearGradient>
    </defs>
    <rect x="0" y="688" width="1200" height="215" fill="url(#yellowBand)"/>
    <rect x="0" y="688" width="1200" height="10" fill="var(--rule-white)"/>
    <polygon points="0,698 1200,698 1200,722 830,884 0,736" fill="url(#greenBand)"/>
    <polyline points="0,738 830,888 1200,726" fill="none" stroke="var(--rule-white)" stroke-width="6"/>
  </svg>

  <h1 class="headline headline--italic headline--new">IT’S NEW!</h1>
  <p class="headline headline--italic headline--exciting">IT’S EXCITING!</p>
  <p class="headline headline--and">AND IT’S…</p>
  <p class="headline headline--italic headline--opening">OPENING IN MELBOURNE</p>

  <p class="tagline">We just can’t contain ourselves, we have to tell you!</p>

  <p class="footer-detail footer-detail--address">218 Harbourline Rd, Westport, 3019</p>
  <p class="footer-detail footer-detail--web">www.dockhavenly.com.au</p>
</main>
</body>
</html>
```